TKB Roofing Flyer/Mailer to be used to market to Homeowners

We need to create a flyer than can double as a mailer for our roofing business and possibly be used as a door hanger as well. This flyer will advertise our roofing company in a professional way with pictures as well as clear and precise text about who we are and what we offer. We are open to this flyer being a bi-fold or even a tri-fold. There would need to be an area for address if used as a mailer. A majority of our company information can be found on our website at www.tkbroofing-example.com.

Target Market(s)

Home Owners

Industry/Entity Type

Construction

Colors
0255a3
ffffff

Requirements
Must have
• Professional design, pictures, text with info regarding our company. Website: www.tkbroofing-example.com

```html
<!DOCTYPE html>
<html lang="en">
<head>
<meta charset="utf-8">
<title>TKB Roofing Mailer</title>
<link rel="stylesheet" href="https://fonts.googleapis.com/css2?family=Tinos:ital,wght@0,400;0,700;1,400;1,700&display=swap">
<style>
  :root {
    --brand-blue: #0255a3;
    --band-blue: #1f4fa8;
    --white: #ffffff;
    --paper: #f1f2f6;
    --paper-shade: #d6d9e1;
    --ink: #2a2d33;
    --rule: #9aa0aa;
    --stage: #2b2b2d;
  }
  * { box-sizing: border-box; margin: 0; padding: 0; }
  html, body { width: 1200px; height: 789px; overflow: hidden; }
  body { background: var(--stage); font-family: "Tinos", "Times New Roman", serif; color: var(--ink); position: relative; }

  .spread { position: absolute; left: 60px; top: 44px; width: 1080px; height: 700px; box-shadow: 0 10px 30px rgba(0,0,0,.5); overflow: hidden; }

  .page-bg { position: absolute; top: 0; width: 540px; height: 700px; }
  .page-bg--back { left: 0; background: linear-gradient(135deg, var(--white) 0%, var(--paper) 45%, var(--paper-shade) 100%); }
  .page-bg--front { left: 540px; background: var(--white); }
  .hero-photo { position: absolute; left: 0; top: 0; width: 540px; height: 560px; background: linear-gradient(180deg, #4f84d2 0%, #9dbfea 22%, #dfe4e6 36%, #cfc7a6 50%, #b8ad86 64%, #7fa356 80%, #5f8c3c 100%); }

  .band-art { position: absolute; left: 0; top: 0; width: 1080px; height: 700px; }

  .spine { position: absolute; left: 530px; top: 0; width: 20px; height: 700px; background: linear-gradient(90deg, rgba(0,0,0,0) 0%, rgba(0,0,0,.12) 50%, rgba(0,0,0,0) 100%); }

  .page { position: absolute; top: 0; width: 540px; height: 700px; }
  .page--back { left: 0; }
  .page--front { left: 540px; }

  .about { position: absolute; left: 40px; top: 44px; width: 250px; }
  .about__title { font-size: 19px; font-weight: 400; padding-bottom: 4px; border-bottom: 1.5px solid var(--brand-blue); }
  .about__title span { color: var(--brand-blue); }
  .about__text { margin-top: 10px; font-size: 10.5px; line-height: 14px; text-align: justify; }

  .postal-stamp, .postal-address { position: absolute; border: 1px solid var(--rule); color: #8a909a; font-family: Arial, sans-serif; font-size: 10px; text-align: center; display: flex; align-items: center; justify-content: center; letter-spacing: .5px; }
  .postal-stamp { left: 410px; top: 40px; width: 90px; height: 62px; }
  .postal-address { left: 310px; top: 118px; width: 200px; height: 96px; }

  .owner { position: absolute; width: 220px; }
  .owner--evan { left: 300px; top: 240px; }
  .owner--dale { left: 40px; top: 300px; }
  .owner__head { display: flex; align-items: center; gap: 10px; }
  .owner__portrait { width: 46px; height: 46px; border-radius: 50%; border: 3px solid var(--brand-blue); background: radial-gradient(circle at 50% 40%, #c9cbd0, #6e7178); flex: none; }
  .owner__name { font-size: 15px; letter-spacing: .5px; line-height: 17px; }
  .owner__role { font-size: 14px; font-weight: 700; font-style: italic; color: var(--brand-blue); letter-spacing: 1px; }
  .owner__bio { margin-top: 8px; font-size: 10.5px; line-height: 14px; text-align: justify; }

  .wordmark { color: var(--brand-blue); text-align: center; }
  .wordmark--small { position: absolute; left: 200px; top: 548px; width: 100px; }
  .wordmark--small .wordmark__name { font-size: 30px; line-height: 30px; letter-spacing: 1px; }
  .wordmark--small .wordmark__sub { font-size: 7px; }
  .wordmark--large { position: absolute; left: 290px; top: 540px; width: 230px; }
  .wordmark--large .wordmark__name { font-size: 70px; line-height: 66px; letter-spacing: 2px; }
  .wordmark--large .wordmark__sub { font-size: 12px; }

  .visit { position: absolute; left: 310px; top: 540px; width: 220px; font-size: 11.5px; line-height: 15px; }
  .visit__hours { color: var(--brand-blue); font-weight: 700; margin-top: 3px; }
  .visit__social { display: flex; gap: 8px; margin-top: 6px; }
  .visit__social span { width: 16px; height: 16px; border-radius: 50%; background: var(--brand-blue); display: block; }
  .icon { width: 11px; height: 11px; vertical-align: -1px; margin-right: 5px; fill: var(--brand-blue); }

  .contact { position: absolute; left: 150px; top: 618px; font-size: 12px; line-height: 17px; font-weight: 700; }
  .contact__phone { font-size: 19px; color: var(--brand-blue); line-height: 24px; }

  .headline { position: absolute; left: 0; top: 54px; width: 540px; text-align: center; color: var(--white); text-shadow: 0 1px 3px rgba(0,0,0,.35); font-weight: 400; }
  .headline__top { font-size: 26px; font-weight: 700; letter-spacing: 1px; }
  .headline__bottom { font-size: 25px; letter-spacing: 1.5px; }

  .front-web { position: absolute; left: 60px; top: 640px; font-size: 13px; font-weight: 700; }
</style>
</head>
<body>
<main class="spread">
  <div class="page-bg page-bg--back"></div>
  <div class="page-bg page-bg--front">
    <div class="hero-photo" role="img" aria-label="Photo of a large two-storey family home with gabled roofs, a front porch and landscaped lawn under a blue sky"></div>
  </div>

  <svg class="band-art" viewBox="0 0 1080 700" aria-hidden="true">
    <polygon points="0,676 260,536 540,536 540,700 0,700" fill="#e9ebf0"/>
    <polygon points="0,640 260,500 540,500 540,536 260,536 0,676" fill="#1f4fa8"/>
    <polygon points="390,700 540,598 540,640 452,700" fill="#1f4fa8"/>
    <polygon points="540,540 860,410 1080,450 1080,700 540,700" fill="#ffffff"/>
    <polygon points="540,500 860,370 1080,410 1080,450 860,410 540,540" fill="#1f4fa8"/>
  </svg>

  <div class="spine"></div>

  <section class="page page--back">
    <article class="about">
      <h2 class="about__title">About <span>TKB</span></h2>
      <p class="about__text">The team here at TKB is a hardworking group of licensed, bonded and insured contractors with more than 25 years of experience. We are a locally owned and operated company dedicated to providing the highest standards of excellence in the roofing and siding service industry here in Indiana. We serve residential and commercial properties with superior workmanship and customer service at an affordable price. Call our office to schedule a free in-home consultation with one of our roofing contractors about your exterior home improvement needs.</p>
    </article>
    <div class="postal-stamp">POSTAL<br>STAMP</div>
    <div class="postal-address">POSTAL<br>ADDRESS</div>

    <div class="owner owner--evan">
      <div class="owner__head">
        <div class="owner__portrait" role="img" aria-label="Portrait of owner Evan Pruitt"></div>
        <div><div class="owner__name">EVAN PRUITT</div><div class="owner__role">OWNER</div></div>
      </div>
      <p class="owner__bio">Evan is a professional contractor with over 20 years of residential construction experience. Prior to joining TKB, he held a senior management role with one of Indiana's most respected builders, working in sales, construction and operations. He and his wife are devoted parents and active members of their church community who value integrity and hard work.</p>
    </div>
    <div class="owner owner--dale">
      <div class="owner__head">
        <div class="owner__portrait" role="img" aria-label="Portrait of owner Dale Hartwell"></div>
        <div><div class="owner__name">DALE HARTWELL</div><div class="owner__role">OWNER</div></div>
      </div>
      <p class="owner__bio">Dale has over 20 years of residential construction and customer service experience. Before starting TKB, he held a senior management role with one of the nation's largest home builders, where his focus was customer satisfaction. This experience makes him a leader in the home improvement field. He is married with two kids and loves spending quality time with his family.</p>
    </div>

    <div class="wordmark wordmark--small">
      <div class="wordmark__name">TKB</div>
      <div class="wordmark__sub">Tri-County Keystone Builders</div>
    </div>

    <div class="visit">
      <div><svg class="icon" viewBox="0 0 10 10"><path d="M5 0a3.5 3.5 0 0 0-3.5 3.5C1.5 6 5 10 5 10s3.5-4 3.5-6.5A3.5 3.5 0 0 0 5 0zm0 5a1.5 1.5 0 1 1 0-3 1.5 1.5 0 0 1 0 3z"/></svg>418 Orchard Lane, Carmel, IN 46032</div>
      <div class="visit__hours">Open Monday - Saturday</div>
      <div>8:00 am - 8:00 pm</div>
      <div class="visit__social"><span></span><span></span></div>
    </div>

    <div class="contact">
      <div class="contact__phone"><svg class="icon" viewBox="0 0 10 10"><path d="M2 0l2 2.3-1 1.2a6 6 0 0 0 3.5 3.5l1.2-1L10 8l-1.2 1.8C4.5 10 0 5.5.2 1.2z"/></svg>555-014-2290</div>
      <div>info@tkbroofing-example.com</div>
      <div>www.tkbroofing-example.com</div>
    </div>
  </section>

  <section class="page page--front">
    <h1 class="headline">
      <div class="headline__top">INDY'S PREMIER</div>
      <div class="headline__bottom">ROOFING CONTRACTORS</div>
    </h1>
    <div class="wordmark wordmark--large">
      <div class="wordmark__name">TKB</div>
      <div class="wordmark__sub">Tri-County Keystone Builders</div>
    </div>
    <div class="front-web"><svg class="icon" viewBox="0 0 10 10"><circle cx="5" cy="5" r="4.3" fill="none" stroke="#0255a3" stroke-width="1.2"/><path d="M.7 5h8.6M5 .7v8.6" stroke="#0255a3" stroke-width="1"/></svg>www.tkbroofing-example.com</div>
  </section>
</main>
</body>
</html>
```